Copperfox Billboard

Please design a billboard using my photos and logos.
For photo of truck please crop the truck itself out and not have the trees / dirt in photo.
Please put " Best Prices in Sevier County"
Please put " 30-yard Dumpsters Starting at 600.00"
Please put " 16-yard Dumpsters Starting at 300.0"
Please put " Delivery and Pickup 7 Days a week"
Billboard size will be 10 ft tall 30 ft wide

```html
<!DOCTYPE html>
<html lang="en">
<head>
<meta charset="utf-8">
<title>Copperfox Dumpsters Billboard</title>
<link rel="stylesheet" href="https://fonts.googleapis.com/css2?family=Bebas+Neue&family=Montserrat:wght@700;800&display=swap">
<style>
  :root {
    --purple: #7e3a96;
    --purple-deep: #4a1d63;
    --black: #0d0d0d;
    --white: #ffffff;
    --stage: #e9eaee;
  }
  * { box-sizing: border-box; margin: 0; padding: 0; }
  html, body { width: 1200px; height: 900px; overflow: hidden; background: var(--stage); }
  .billboard {
    position: absolute; left: 30px; top: 260px;
    width: 1140px; height: 380px;
    background: var(--white); overflow: hidden;
    font-family: "Montserrat", sans-serif;
  }
  .billboard__shapes { position: absolute; inset: 0; }
  .headline {
    position: absolute; left: 48px; top: 24px;
    font-family: "Bebas Neue", sans-serif;
    font-size: 84px; line-height: 0.86; color: var(--black);
  }
  .headline__accent { color: var(--purple); }
  .offer {
    position: absolute; left: 48px; height: 44px; width: 314px;
    display: flex; align-items: center; padding: 0 9px;
    font-weight: 800; font-size: 26px; color: var(--white);
  }
  .offer--large { top: 173px; background: var(--purple); }
  .offer--small { top: 226px; background: var(--black); }
  .price { position: absolute; left: 376px; font-weight: 800; }
  .price__label { font-size: 15px; color: var(--black); display: flex; align-items: center; gap: 5px; }
  .price__label::after {
    content: ""; border-left: 9px solid var(--purple);
    border-top: 6px solid transparent; border-bottom: 6px solid transparent;
  }
  .price__amount { font-size: 31px; line-height: 1; color: var(--purple); }
  .price--large { top: 172px; }
  .price--small { top: 225px; }
  .badge__title {
    position: absolute; left: 484px; top: 38px; width: 150px;
    text-align: center; font-weight: 800; font-size: 22px; line-height: 0.95;
    color: var(--white);
  }
  .badge__tag {
    position: absolute; left: 480px; top: 111px; width: 152px; height: 27px;
    background: var(--black); color: var(--white);
    font-weight: 800; font-size: 15px; text-align: center; line-height: 27px;
    white-space: nowrap;
  }
  .call {
    position: absolute; left: 48px; top: 306px;
    font-weight: 800; font-size: 55px; line-height: 1; color: var(--white);
    white-space: nowrap;
  }
  .truck-photo {
    position: absolute; left: 655px; top: 40px; width: 445px; height: 238px;
    border-radius: 24px;
    background: linear-gradient(100deg, #f4f4f6 0%, #d9dbe0 45%, var(--purple-deep) 75%, #2b1040 100%);
  }
  .brand {
    position: absolute; left: 820px; top: 286px; width: 293px;
    font-weight: 800; color: var(--white); text-align: right; line-height: 1;
  }
  .brand__name { font-size: 40px; letter-spacing: 1px; }
  .brand__sub { font-size: 23px; letter-spacing: 2px; margin-top: 4px; }
</style>
</head>
<body>
  <main class="billboard">
    <svg class="billboard__shapes" width="1140" height="380" viewBox="0 0 1140 380">
      <path d="M0 284 L715 298 L745 380 L0 380 Z" fill="var(--black)"/>
      <path d="M765 0 L792 0 C722 110 727 300 782 380 L740 380 C690 300 690 110 765 0 Z" fill="var(--black)"/>
      <path d="M800 0 L1140 0 L1140 380 L792 380 C737 300 732 110 800 0 Z" fill="var(--purple)"/>
      <path d="M471 18 L643 13 L632 158 L558 165 L552 217 L520 190 L482 150 Z" fill="var(--purple)"/>
      <path d="M520 190 L552 217 L590 165 L558 165 Z" fill="var(--black)"/>
    </svg>

    <h1 class="headline"><span class="headline__accent">Best Prices</span> In<br>Sevier County</h1>

    <div class="offer offer--large">30-yard Dumpsters</div>
    <div class="price price--large"><div class="price__label">Starting at</div><div class="price__amount">600.00</div></div>

    <div class="offer offer--small">16-yard Dumpsters</div>
    <div class="price price--small"><div class="price__label">Starting at</div><div class="price__amount">300.00</div></div>

    <div class="badge__title">Delivery<br>and<br>Pickup</div>
    <div class="badge__tag">7 Days a week</div>

    <p class="call">Call us 0198-765-432</p>

    <div class="truck-photo" role="img" aria-label="Photo of a white roll-off truck carrying a purple dumpster"></div>

    <div class="brand">
      <div class="brand__name">COPPERFOX</div>
      <div class="brand__sub">DUMPSTERS</div>
    </div>
  </main>
</body>
</html>
```